Flyer for annual LUMEN SUMMIT 2020

I would like a church event flyer designed. The event is called "LUMEN SUMMIT 2020". I am looking for a professional, yet catchy design that uses our brand colors and logo creatively while communicating key information of the event effectively.

1. The logo is attached in two color formats. The designer has the choice to use them as he/she want.

2. The location of the event is: Talbot Community Center, 482 Wexley Street, Portland, ME 04107

3. Time and date of event. The designer can organize and format the date and time as he/she pleases.
Thursday December 31st @ 6:30PM
Friday January 1st @ 6:30PM
Saturday 2nd @ 6:30PM
Sunday 3rd @ 4:30PM

4. The topic of the event is "Deep Wells and Tall Cedars". The designer is free to use this phrase as he/she pleases to create a good composition.

5. Speaker: Prophet Marcus Obuya (2 pictures of the speaker to choose from are attached)

6. Contact information: contact@harborvine.org - Telephone number: 207 583 2194

7. I would also like the following three words on the flyer. These words describe the focus of the event: FIRE, REVIVAL, PROPHETIC

Target Market(s)

Young adults

Font styles to use
Sans Serif

Requirements
Must have
• Logo, speaker's picture
Should not have
• cross image, church image

```html
<!DOCTYPE html>
<html lang="en">
<head>
<meta charset="utf-8">
<title>Lumen Summit 2020 Flyer</title>
<link rel="stylesheet" href="https://fonts.googleapis.com/css2?family=Roboto:ital,wght@0,500;0,700;1,700&display=swap">
<style>
  :root {
    --navy: #023a5e;
    --orange: #d07400;
    --orange-text: #e07c0c;
    --white: #ffffff;
    --photo-light: #a49d95;
    --photo-dark: #4d4742;
  }
  * { margin: 0; padding: 0; box-sizing: border-box; }
  html, body { width: 848px; height: 1200px; overflow: hidden; background: var(--white); }
  body { font-family: "Roboto", Arial, sans-serif; color: var(--navy); }
  .flyer { position: relative; width: 848px; height: 1200px; overflow: hidden; background: var(--white); }

  .brand-panel {
    position: absolute; left: 173px; top: 0; width: 508px; height: 256px;
    background: var(--navy); border-radius: 0 0 62px 62px;
    display: flex; flex-direction: column; align-items: center; justify-content: center;
  }
  .brand-name { font-weight: 700; font-size: 82px; letter-spacing: 4px; color: var(--white); line-height: 1; margin-top: 40px; }
  .brand-tagline { font-weight: 500; font-size: 21px; letter-spacing: 1px; color: var(--orange-text); margin-top: 10px; }

  .shape { position: absolute; left: 0; top: 0; }

  .event-title {
    position: absolute; left: 136px; top: 287px; width: 712px; height: 88px;
    display: flex; align-items: center; justify-content: center;
    font-weight: 700; font-size: 42px; color: var(--white); padding-left: 30px;
  }
  .event-theme {
    position: absolute; left: 0; top: 390px; width: 300px; height: 72px;
    display: flex; align-items: center; padding-left: 38px;
    font-weight: 500; font-size: 23px; line-height: 27px; color: var(--white);
  }

  .schedule { position: absolute; left: 0; top: 475px; width: 369px; text-align: center; }
  .month-bar {
    height: 35px; background: var(--navy); color: var(--white);
    font-weight: 700; font-size: 21px; letter-spacing: 8px; line-height: 35px; padding-left: 8px;
  }
  .session-list { padding: 4px 0 5px; }
  .session { font-weight: 700; font-size: 21px; line-height: 31.4px; }

  .focus-words {
    position: absolute; left: 65px; top: 824px; width: 247px; height: 157px;
    display: flex; flex-direction: column; align-items: center; justify-content: center;
    font-weight: 700; font-size: 41px; line-height: 47px; color: var(--orange-text); letter-spacing: -1px;
  }

  .venue {
    position: absolute; left: 0; top: 990px; width: 370px; text-align: center;
    font-weight: 700; font-size: 20px; line-height: 29.5px; font-style: normal;
  }

  .speaker-photo {
    position: absolute; left: 370px; top: 375px; width: 478px; height: 717px;
    background:
      radial-gradient(ellipse 55% 60% at 55% 62%, #c8501f 0%, #b44718 55%, rgba(180,71,24,0) 72%),
      radial-gradient(ellipse at 50% 40%, var(--photo-light) 0%, var(--photo-dark) 100%);
  }

  .contact {
    position: absolute; left: 0; top: 1092px; width: 370px; height: 108px;
    background: var(--orange); color: var(--white);
    display: flex; flex-direction: column; align-items: center; justify-content: center;
    font-weight: 700; font-size: 20px; line-height: 28px; padding-bottom: 6px;
  }
  .speaker-name {
    position: absolute; left: 370px; top: 1092px; width: 478px; height: 108px;
    background: var(--navy); color: var(--white);
    display: flex; align-items: center; justify-content: center;
    font-weight: 700; font-style: italic; font-size: 31px; padding-bottom: 8px;
  }
</style>
</head>
<body>
<main class="flyer">
  <header class="brand-panel">
    <div class="brand-name">KAVELO</div>
    <div class="brand-tagline">A LIGHT TO EVERY PEOPLE</div>
  </header>

  <svg class="shape" width="848" height="1200" viewBox="0 0 848 1200" aria-hidden="true">
    <polygon points="136,287 848,287 848,375 32,375" fill="var(--navy)"/>
    <polygon points="0,390 290,390 342,462 0,462" fill="var(--orange)"/>
    <rect x="66" y="825" width="245" height="155" fill="none" stroke="var(--orange-text)" stroke-width="5" stroke-dasharray="0 12.4" stroke-linecap="round"/>
  </svg>

  <h1 class="event-title">LUMEN SUMMIT 2020</h1>
  <h2 class="event-theme">DEEP WELLS AND<br>TALL CEDARS</h2>

  <section class="schedule">
    <div class="month-bar">DECEMBER</div>
    <div class="session-list">
      <p class="session">Thursday 31st</p>
      <p class="session">@ 6:30PM</p>
    </div>
    <div class="month-bar">JANUARY</div>
    <div class="session-list">
      <p class="session">Friday 1st</p>
      <p class="session">@ 6:30PM</p>
      <p class="session">Saturday 2nd</p>
      <p class="session">@ 6:30PM</p>
      <p class="session">Sunday 3rd</p>
      <p class="session">@ 4:30PM</p>
    </div>
  </section>

  <div class="focus-words">
    <span>FIRE</span>
    <span>REVIVAL</span>
    <span>PROPHETIC</span>
  </div>

  <address class="venue">
    Talbot Community Center, 482<br>Wexley Street,<br>Portland, ME 04107
  </address>

  <div class="speaker-photo" role="img" aria-label="Portrait of the speaker in an orange blazer against a grey brick wall"></div>

  <footer class="contact">
    <span>contact@harborvine.org</span>
    <span>Telephone number: 207 583 2194</span>
  </footer>
  <div class="speaker-name">PROPHET MARCUS OBUYA</div>
</main>
</body>
</html>
```